Website Design

Hi I would like to invite designers to re design my website .

I would like the below in brief.

On the Welcome Page.

A nice looking technical page distributed into two

SALES on one side and TECHNOLOGY on the other . once the person clicks on either of them they can explore the pages in detail.

I am keen and almost ready with information for the Technology page and would like this to begin kicking ASAP .

my current website is www.brimvoltek.net

Looking forward to seeing your feedback!

Tobiah
Updates

Hi,

 
A little more elaboration on the web front page . I need it to be more techy .

I was looking at a wheel on the Technical side or a spanner and screew driver done on flash .

Just to give you a better idea on what seperated Sales from Technology. 

Computing, Storage , Components , Peripherals , Software , TV & Gaming / Entertainment , Home & Leisure , Software , Gift Vouchers , Phones etc.

Technology .

Solar Power Solutions , Security Systems , Access Control , Automatic Gates & Turnstiles , Home/Office/Hotel Automation, Indoor and Outdoor PABX Telephony, Networking , Electricity Power Meters , IP Based Technology and ETC. 

See attached on the project updates my business card design if it can give you an idea ,also see revised Logo

```html
<!DOCTYPE html>
<html lang="en">
<head>
<meta charset="utf-8">
<title>Brimvoltek — Welcome</title>
<link rel="stylesheet" href="https://fonts.googleapis.com/css2?family=Oswald:wght@500;700&family=Roboto:wght@400;500&display=swap">
<style>
  :root {
    --page-bg: #f4f4f4;
    --page-grain: #ececec;
    --brand-red: #d21b0d;
    --nav-divider: #e8483c;
    --ink-dark: #2a2a2a;
    --label-grey: #b9b9b9;
    --icon-white: #f5f5f5;
    --footer-text: #e6e6e6;
    --rule: #d6d6d6;
    --social-ring: #6a6a6a;
    --social-fill: #3a3a3a;
  }
  * { box-sizing: border-box; margin: 0; padding: 0; }
  html, body { width: 1200px; height: 675px; overflow: hidden; }
  body {
    position: relative;
    font-family: "Roboto", Arial, sans-serif;
    background-color: var(--page-bg);
    background-image: repeating-linear-gradient(90deg, transparent 0 3px, rgba(0,0,0,0.018) 3px 4px, transparent 4px 9px);
  }
  .site-header { position: absolute; top: 0; left: 0; width: 1200px; height: 137px; }
  .brand-name {
    position: absolute; top: 28px; left: 0; width: 1200px; text-align: center;
    font-family: "Oswald", sans-serif; font-weight: 700; font-size: 56px;
    letter-spacing: 1px; color: var(--brand-red);
  }
  .main-nav {
    position: absolute; top: 137px; left: 0; width: 1200px; height: 33px;
    background: var(--brand-red);
  }
  .main-nav ul { position: absolute; left: 362px; top: 0; display: flex; list-style: none; height: 33px; }
  .main-nav li {
    height: 33px; line-height: 33px; font-size: 13px; color: #fff;
    text-align: center; border-right: 1px solid var(--nav-divider);
  }
  .main-nav li:last-child { border-right: none; }
  .main-nav li.is-current { background: var(--ink-dark); border-right: none; }
  .nav-home { width: 79px; }
  .nav-about { width: 87px; }
  .nav-sales { width: 85px; }
  .nav-tech { width: 127px; }
  .nav-contact { width: 95px; }
  .division-card { position: absolute; top: 234px; width: 198px; height: 240px; }
  .division-card.sales { left: 352px; }
  .division-card.technology { left: 651px; }
  .division-disc {
    width: 198px; height: 198px; border-radius: 50%; background: var(--ink-dark);
    position: relative;
  }
  .division-disc svg { position: absolute; left: 64px; top: 46px; }
  .division-label {
    position: absolute; top: 132px; left: 0; width: 198px; text-align: center;
    font-family: "Oswald", sans-serif; font-weight: 700; font-size: 20px;
    color: var(--label-grey); letter-spacing: -0.3px;
  }
  .division-shadow {
    position: absolute; top: 218px; left: 48px; width: 102px; height: 10px;
    border-radius: 50%; background: rgba(0,0,0,0.35); filter: blur(4px);
  }
  .content-rule { position: absolute; top: 531px; left: 161px; width: 880px; height: 1px; background: var(--rule); }
  .site-footer { position: absolute; top: 535px; left: 0; width: 1200px; height: 140px; background: var(--ink-dark); }
  .footer-legal {
    position: absolute; top: 36px; left: 0; width: 1200px; text-align: center;
    font-size: 12px; color: var(--footer-text);
  }
  .footer-legal strong { font-weight: 500; }
  .footer-legal .sep { margin: 0 12px; }
  .social-links { position: absolute; top: 75px; left: 545px; display: flex; gap: 10px; list-style: none; }
  .social-links li {
    width: 30px; height: 30px; border-radius: 50%;
    background: var(--social-fill); border: 2px solid var(--social-ring);
  }
</style>
</head>
<body>
  <header class="site-header">
    <div class="brand-name">Brimvoltek</div>
  </header>

  <nav class="main-nav">
    <ul>
      <li class="nav-home is-current">HOME</li>
      <li class="nav-about">ABOUT</li>
      <li class="nav-sales">SALES</li>
      <li class="nav-tech">TECHNOLOGY</li>
      <li class="nav-contact">CONTACT</li>
    </ul>
  </nav>

  <section class="division-card sales">
    <div class="division-disc">
      <svg width="70" height="72" viewBox="0 0 70 72" aria-hidden="true">
        <path d="M24 16 V8 a4 4 0 0 1 4-4 h14 a4 4 0 0 1 4 4 v8 h-6 v-6 h-10 v6 z" fill="var(--icon-white)"/>
        <rect x="0" y="16" width="70" height="54" rx="6" fill="var(--icon-white)"/>
        <rect x="0" y="34" width="70" height="2" fill="var(--ink-dark)"/>
        <rect x="30" y="30" width="10" height="12" rx="2" fill="var(--ink-dark)"/>
      </svg>
      <div class="division-label">SALES</div>
    </div>
    <div class="division-shadow"></div>
  </section>

  <section class="division-card technology">
    <div class="division-disc">
      <svg width="76" height="66" viewBox="0 0 76 66" aria-hidden="true">
        <g fill="var(--icon-white)">
          <path d="M60 4 l6 4 -22 30 -4 -3 z"/>
          <path d="M40 33 l5 4 -22 26 a5 5 0 0 1 -8 -6 z"/>
          <path d="M4 8 a14 14 0 0 0 18 18 l40 34 a5 5 0 0 0 7 -7 l-34 -40 a14 14 0 0 0 -18 -18 l8 8 -2 8 -8 2 z"/>
        </g>
      </svg>
      <div class="division-label">TECHNOLOGY</div>
    </div>
    <div class="division-shadow"></div>
  </section>

  <div class="content-rule"></div>

  <footer class="site-footer">
    <p class="footer-legal">Copyright © <strong>Brimvoltek</strong> 2013<span class="sep">I</span> Terms &amp; Conditions</p>
    <ul class="social-links" aria-label="Social profiles">
      <li></li><li></li><li></li>
    </ul>
  </footer>
</body>
</html>
```